Business Card design for new private practice opening

I need a business card design for my new private practice with my new logo uploaded as a file
On the front the logo
On the back: maybe a small logo somewhere?
Priv. Doz. DDr. Corinna Vestaluk
Fachärztin für Allgemein- & Viszeralchirurgie
Address: xxx
Tel: xxx
Mobil:xxx
Webseite:xxx
Email:xxx

Contact Information for Business Card

See project description above for details

Requirements
Nice to have
• I would like the colors of the logo incorporated into the business card

```html
<!DOCTYPE html>
<html lang="de">
<head>
<meta charset="utf-8">
<title>Visitenkarte – Priv. Doz. DDr. Corinna Vestaluk</title>
<link href="https://fonts.googleapis.com/css2?family=Raleway:wght@400;500;600&display=swap" rel="stylesheet">
<style>
  :root {
    --backdrop: #e5e5e5;
    --card: #ffffff;
    --teal: #52b6ae;
    --grey: #8c8c8c;
    --text-grey: #7a7a7a;
  }
  * { box-sizing: border-box; margin: 0; padding: 0; }
  html, body {
    width: 967px;
    height: 1200px;
    overflow: hidden;
    background: var(--backdrop);
    font-family: "Raleway", sans-serif;
  }
  .canvas { position: relative; width: 967px; height: 1200px; }
  .card {
    position: absolute;
    top: 460px;
    width: 401px;
    height: 269px;
    background: var(--card);
  }
  .card--front { left: 57px; }
  .card--back { left: 507px; }

  .band {
    position: absolute;
    left: 0; right: 0;
    background: var(--teal);
  }
  .band--top { top: 0; height: 8px; }
  .band--bottom { bottom: 0; height: 7px; }

  .brand {
    position: absolute;
    display: flex;
    align-items: center;
    color: var(--teal);
    font-weight: 600;
    white-space: nowrap;
  }
  .brand__dot {
    border-radius: 50%;
    background: var(--teal);
    flex: none;
  }
  .brand--large {
    left: 0; right: 0;
    top: 112px;
    justify-content: center;
    gap: 12px;
    font-size: 24px;
  }
  .brand--large .brand__dot { width: 30px; height: 30px; }
  .brand--small {
    left: 29px;
    top: 40px;
    gap: 8px;
    font-size: 14px;
  }
  .brand--small .brand__dot { width: 18px; height: 18px; }

  .holder__name {
    position: absolute;
    left: 29px;
    top: 114px;
    font-size: 22px;
    font-weight: 500;
    color: var(--grey);
    white-space: nowrap;
  }
  .holder__title {
    position: absolute;
    left: 29px;
    top: 147px;
    font-size: 14.5px;
    font-weight: 400;
    color: var(--teal);
    white-space: nowrap;
  }
  .contact {
    position: absolute;
    left: 29px;
    top: 200px;
    padding-left: 10px;
    border-left: 2px solid var(--teal);
    font-size: 13.5px;
    line-height: 21px;
    color: var(--text-grey);
  }
  .contact__row { white-space: nowrap; }
  .contact__sep {
    display: inline-block;
    width: 2px;
    height: 14px;
    margin: 0 7px;
    background: var(--teal);
    vertical-align: -2px;
  }
</style>
</head>
<body>
<main class="canvas">
  <section class="card card--front" aria-label="Vorderseite">
    <div class="band band--top"></div>
    <div class="brand brand--large">
      <span class="brand__dot"></span>
      <span class="brand__name">Praxis Vestaluk</span>
    </div>
    <div class="band band--bottom"></div>
  </section>

  <section class="card card--back" aria-label="Rückseite">
    <div class="brand brand--small">
      <span class="brand__dot"></span>
      <span class="brand__name">Praxis Vestaluk</span>
    </div>
    <h1 class="holder__name">Priv. Doz. DDr. Corinna Vestaluk</h1>
    <p class="holder__title">Fachärztin für Allgemein- &amp; Viszeralchirurgie</p>
    <div class="contact">
      <p class="contact__row">Address: xxx<span class="contact__sep"></span>Tel: xxx<span class="contact__sep"></span>Mobil: xxx</p>
      <p class="contact__row">Webseite: xxx<span class="contact__sep"></span>Email: xxx</p>
    </div>
    <div class="band band--bottom"></div>
  </section>
</main>
</body>
</html>
```